BRASKETT LAND SERVICES BILLBOARD DESIGN

I NEED A BILLBOARD FOR MY BUSINESS. WE ARE A LAND CLEARING COMPANY AND I WOULD LIKE TO ADD A PICTURE OF MY TRACK LOADER TO THE SIGN. OPEN TO COLORS. I WOULD ALSO LIKE TO HAVE MY PHONE NUMBER 555-284-7196, WEBSITE WWW.BRASKETTLANDSERVICES.EXAMPLE, AND EMAIL ON THE SIGN (CONTACT@BRASKETTLANDSERVICES.EXAMPLE). DESIGNERS CAN HAVE THE FREEDOM TO DO WHATEVER STYLE THEY WANT AND TO USE ANY COLORS THEY WANT.

Target Market(s)

ANYONE WITH PROPERTY

Requirements
Must have
• PICTURE OF TRACK LOADER, WEBSITE, PHONE NUMBER, EMAIL
Nice to have
• OPEN TO ANYTHING
Should not have
• OPEN TO ANYTHING

```html
<!DOCTYPE html>
<html lang="en">
<head>
<meta charset="utf-8">
<title>Braskett Land Services Billboard</title>
<link rel="stylesheet" href="https://fonts.googleapis.com/css2?family=Roboto:ital,wght@0,700;1,700;1,900&display=swap">
<style>
  :root {
    --page: #e9ecf1;
    --ink: #1c1a1a;
    --white: #ffffff;
    --orange: #e8512a;
    --forest-dark: #2f3a22;
    --forest-mid: #5d6a3c;
    --loader-orange: #c9532b;
  }
  html, body {
    margin: 0;
    padding: 0;
    width: 1200px;
    height: 1195px;
    overflow: hidden;
    background: var(--page);
  }
  .billboard {
    position: absolute;
    left: 0;
    top: 447px;
    width: 1200px;
    height: 301px;
    display: block;
  }
  .brand-name { font-family: "Roboto", Arial, sans-serif; font-weight: 900; font-style: italic; fill: var(--ink); }
  .brand-sub { font-family: "Roboto", Arial, sans-serif; font-weight: 700; font-style: italic; fill: var(--ink); }
  .call-now { font-family: "Roboto", Arial, sans-serif; font-weight: 700; font-style: italic; fill: var(--orange); }
  .phone { font-family: "Roboto", Arial, sans-serif; font-weight: 700; fill: var(--white); }
  .contact-email { font-family: "Roboto", Arial, sans-serif; font-weight: 700; font-style: italic; fill: var(--white); }
  .contact-web { font-family: "Roboto", Arial, sans-serif; font-weight: 700; font-style: italic; fill: var(--orange); }
</style>
</head>
<body>
<svg class="billboard" viewBox="0 0 1200 301" xmlns="http://www.w3.org/2000/svg">
  <defs>
    <linearGradient id="loaderPhotoTone" x1="0" y1="0" x2="1" y2="1">
      <stop offset="0" stop-color="#3b4a2a"/>
      <stop offset="0.35" stop-color="#6b5a3a"/>
      <stop offset="0.55" stop-color="#b2522c"/>
      <stop offset="1" stop-color="#4f5436"/>
    </linearGradient>
  </defs>

  <rect class="panel-white" x="0" y="0" width="1200" height="301" fill="var(--white)"/>

  <polygon class="loader-photo" role="img" aria-label="Photo of an orange tracked loader with a forestry mulcher head in a wooded clearing"
           points="0,0 652,0 540,301 0,301" fill="url(#loaderPhotoTone)"/>

  <polygon class="contact-band" points="0,236 563,236 540,301 0,301" fill="var(--ink)"/>

  <polygon class="accent-stripe" points="652,0 685,0 573,301 540,301" fill="var(--orange)"/>

  <polygon class="accent-slant" points="632,168 654,168 620,258 598,258" fill="var(--ink)"/>

  <polygon class="phone-tab" points="702,240 1058,240 1078,284 1200,284 1200,301 573,301 579,284 682,284" fill="var(--ink)"/>

  <text class="brand-name" x="700" y="132" font-size="92" textLength="484" lengthAdjust="spacingAndGlyphs">BRASKETT</text>
  <text class="brand-sub" x="663" y="191" font-size="52" textLength="462" lengthAdjust="spacingAndGlyphs">LAND SERVICES</text>
  <text class="call-now" x="888" y="236" font-size="34" text-anchor="middle">Call Now</text>
  <text class="phone" x="888" y="293" font-size="58" text-anchor="middle" textLength="344" lengthAdjust="spacingAndGlyphs">555-284-7196</text>

  <text class="contact-email" x="40" y="263" font-size="20" textLength="441" lengthAdjust="spacingAndGlyphs">CONTACT@BRASKETTLANDSERVICES.EXAMPLE</text>
  <text class="contact-web" x="40" y="292" font-size="20" textLength="380" lengthAdjust="spacingAndGlyphs">WWW.BRASKETTLANDSERVICES.EXAMPLE</text>
</svg>
</body>
</html>
```